Postcard Design

I need a postcard style insert designed that will be mailed out with a customer's monthly statement. This postcard will describe a new service offered to the customer by our company. The front of the postcard will have a design layout of the word definition for "Monetize" and similar to design layout used in a dictionary (i.e., enunciation, Verb, definition, and sample of how word is used). The backside of card will have brief description of service offered and contact information for my office.

Industry/Entity Type

It Company

```html
<!DOCTYPE html>
<html lang="en">
<head>
<meta charset="utf-8">
<title>Monetize Postcard</title>
<link rel="stylesheet" href="https://fonts.googleapis.com/css2?family=Arimo:ital,wght@0,400;0,700;1,400&family=Gochi+Hand&family=Open+Sans:wght@400&display=swap">
<style>
  :root {
    --stage: #333333;
    --front-red: #ea0601;
    --accent-gold: #f9c12c;
    --front-text: #fde9d9;
    --back-paper: #e4e4e4;
    --back-edge: #c9c9c9;
    --back-text: #6e6e6e;
    --brand-navy: #1d1b45;
  }
  * { margin: 0; padding: 0; box-sizing: border-box; }
  html, body {
    width: 1200px; height: 652px; overflow: hidden;
    background: var(--stage);
  }
  .postcard {
    position: absolute; left: 123px; top: 142px;
    width: 953px; height: 367px;
    display: flex;
  }
  .front {
    width: 477px; height: 100%;
    background: var(--front-red);
    position: relative;
  }
  .headword {
    position: absolute; left: 80px; top: 96px;
    font-family: "Gochi Hand", cursive;
    font-size: 64px; line-height: 1;
    color: var(--accent-gold);
    letter-spacing: 0.5px;
  }
  .entry {
    position: absolute; left: 160px; top: 178px;
    font-family: "Arimo", Arial, sans-serif;
  }
  .pronunciation {
    color: var(--accent-gold); font-size: 13px;
    display: flex; align-items: center; gap: 3px;
  }
  .pronunciation svg { width: 10px; height: 10px; }
  .part-of-speech {
    color: var(--accent-gold); font-style: italic;
    font-size: 13px; margin-top: 8px;
  }
  .senses {
    list-style: none; margin-top: 6px;
    color: var(--front-text); font-size: 11px; line-height: 17px;
  }
  .senses li { padding-left: 8px; text-indent: -8px; }
  .back {
    flex: 1; height: 100%;
    background: var(--back-paper);
    border: 1px solid var(--back-edge); border-left: none;
    position: relative;
  }
  .pitch {
    position: absolute; left: 33px; top: 37px;
    font-family: "Arimo", Arial, sans-serif;
    font-size: 11px; line-height: 16.4px;
    color: var(--back-text);
  }
  .brand {
    position: absolute; left: 40px; top: 268px;
    display: flex; align-items: center; gap: 8px;
    font-family: "Arimo", Arial, sans-serif;
    font-weight: 700; font-size: 17px;
    color: var(--brand-navy);
  }
  .brand-mark { width: 14px; height: 14px; background: var(--brand-navy); }
  .privacy-note {
    position: absolute; left: 39px; top: 332px;
    font-family: "Open Sans", Arial, sans-serif;
    font-size: 8.3px; color: var(--back-text);
    white-space: nowrap;
  }
</style>
</head>
<body>
  <main class="postcard">
    <section class="front">
      <h1 class="headword">mon•e•tize</h1>
      <div class="entry">
        <p class="pronunciation">/ˋmane.tiz/
          <svg viewBox="0 0 10 10" aria-hidden="true"><path d="M1 3.5h2l2.5-2.2v7.4L3 6.5H1z" fill="currentColor"/><path d="M7 3.2a2.4 2.4 0 0 1 0 3.6M8.3 2a4 4 0 0 1 0 6" stroke="currentColor" fill="none" stroke-width="0.9"/></svg>
        </p>
        <p class="part-of-speech">verb</p>
        <ol class="senses">
          <li>1.Convert into or express in the form of currency.</li>
          <li>2.Convert real estate contract into currency that<br>&nbsp;&nbsp;can be used to purchase goods and services</li>
        </ol>
      </div>
    </section>
    <section class="back">
      <p class="pitch">Interested in knowing what your<br>real estate contract is worth if you<br>were to sell it for a lump sum<br>cash payment?<br>Call Ledgerline Capital today<br>at 208-555-0143<br>for a free no-obligation quote<br>on the cash value of your contract.</p>
      <div class="brand"><span class="brand-mark"></span>Keystone Realty</div>
      <p class="privacy-note">Your privacy is assured.&nbsp; Your escrow servicing providing this opportunity to you as a confidential courtesy</p>
    </section>
  </main>
</body>
</html>
```